Very Simple Web Redesign Project - Using Photoshop

Required is a very simple website home page redesign for the following site: http://www.tallowcrestslate.com.au/
I require this as a Photoshop design.
The basic look and feel of the site needs to remain.
Specifically the colours don't need to be changed.
The positioning of the site is currently correct for the target market.
The site does not need to be made super slick looking. Just upgraded to a new version.
The current text can all be used.
The only menus necessary are a horizontal menu at the top, and a simple horizontal text menu at the bottom of the page. Do NOT retain the vertical menu on the home page (having the items "Our Gallery", "Our Services", "Enquire Now").
Give the horizontal menu the following items:
Home | Slate Roof Repairs | Slate Reroofing | Slate Roof Benefits | Other Services | Photo Gallery | FAQ's | Free Quote | Contact Us
The picture of the house at the top RHS of the page needs to be reduced in size by approx 50% and moved to the top LHS of the page.
Please place the following text into the top of the page:
"Call Now: 0427 618 392"
Keep the four pictures on the home page layout. Some larger images attached.
Thanks,
Rob
Updates
Hi,
Thanks for all the designs.
I am working with my client to get which one they like the most.
Thanks,
Rob

```html
<!DOCTYPE html>
<html lang="en">
<head>
<meta charset="utf-8">
<title>Tallowcrest Slate - the Slate Roof Specialists</title>
<link rel="stylesheet" href="https://fonts.googleapis.com/css2?family=Oswald:wght@400&family=Noto+Sans:wght@400&display=swap">
<style>
:root{
  --green-dark:#3a7320;
  --green-mid:#4a8c27;
  --green-text:#356a1c;
  --nav-active:#4d8f24;
  --band-dark:#262626;
  --panel:#ebebeb;
  --ink:#222;
  --muted:#aaa;
  --white:#fff;
  --rule:#ddd;
}
*{margin:0;padding:0;box-sizing:border-box}
html,body{width:1200px;height:1125px;overflow:hidden;background:var(--white)}
body{position:relative;font-family:"Noto Sans",sans-serif;color:var(--ink)}
.header{position:absolute;left:0;top:0;width:1200px;height:215px;background:linear-gradient(180deg,var(--green-dark),var(--green-mid))}
.header svg{position:absolute;left:0;top:0}
.dark-band{position:absolute;left:0;top:215px;width:1200px;height:487px;background:var(--band-dark)}
.brand{position:absolute;left:122px;top:52px;display:flex;align-items:center;gap:22px}
.brand-mark{width:50px;height:50px;background:#2c5a18;border:2px solid rgba(255,255,255,.6)}
.brand-name{font-family:"Oswald",sans-serif;font-size:48px;color:var(--white);line-height:1}
.call-now{position:absolute;right:120px;top:64px;font-family:"Oswald",sans-serif;font-size:28px;color:var(--white)}
.page{position:absolute;left:120px;top:157px;width:960px;height:893px;background:var(--white);box-shadow:0 0 4px rgba(0,0,0,.35)}
.nav{position:absolute;left:0;width:960px;height:58px;background:linear-gradient(180deg,#fff,#ececec);display:flex;align-items:center;padding-left:29px;font-size:14px}
.nav a{color:var(--ink);text-decoration:none}
.nav a.active{color:var(--nav-active)}
.nav span.sep{display:inline-block;width:1px;height:10px;border-left:1px dotted #aaa;margin:0 10px}
.nav-top{top:0;border-bottom:1px solid var(--rule)}
.nav-bottom{top:834px;border-top:1px solid var(--rule)}
.main-title{position:absolute;left:29px;top:72px;font-family:"Oswald",sans-serif;font-weight:400;font-size:34px;color:var(--green-text);line-height:44px}
.photo{position:absolute;border:3px solid var(--white);box-shadow:0 0 3px rgba(0,0,0,.45)}
.intro{position:absolute;left:30px;top:413px;width:550px;font-size:15.5px;line-height:25px}
.intro p{margin-bottom:25px}
.sidebar{position:absolute;left:614px;top:80px;width:316px;height:724px;background:var(--panel);padding:0 18px}
.sidebar h2{margin-top:54px;font-family:"Oswald",sans-serif;font-weight:400;font-size:22px;color:var(--green-text)}
.sidebar .area{margin-top:14px;font-size:13.5px;line-height:19px}
.contact-line{font-family:"Oswald",sans-serif;font-size:22px;line-height:28px;color:var(--ink)}
.contact-line .label{color:var(--green-text)}
.contacts{margin-top:94px}
.reg{margin-top:16px;font-size:13px;line-height:19px;color:var(--muted)}
.copyright{position:absolute;left:149px;top:1073px;font-size:11.5px;color:var(--green-text)}
</style>
</head>
<body>
<div class="header">
  <svg width="1200" height="215" aria-hidden="true">
    <path d="M0 60 C300 20 520 30 760 90 S1050 160 1200 120 L1200 0 L0 0 Z" fill="rgba(255,255,255,.05)"/>
  </svg>
  <div class="brand"><div class="brand-mark"></div><div class="brand-name">Tallowcrest Slate</div></div>
  <div class="call-now">Call Now: 0427 618 392</div>
</div>
<div class="dark-band"></div>

<div class="page">
  <nav class="nav nav-top">
    <a class="active">Home</a><span class="sep"></span><a>Slate Roof Repairs</a><span class="sep"></span><a>Slate Reroofing</a><span class="sep"></span><a>Slate Roof Benefits</a><span class="sep"></span><a>Other Services</a><span class="sep"></span><a>Photo Gallery</a><span class="sep"></span><a>FAQ's</a><span class="sep"></span><a>Free Quote</a><span class="sep"></span><a>Contact Us</a>
  </nav>

  <h1 class="main-title">Tallowcrest Slate - the Slate Roof Specialists</h1>

  <div class="photo" role="img" aria-label="Roofer standing on a brick house roof" style="left:35px;top:143px;width:167px;height:113px;background:linear-gradient(180deg,#dfe4ea,#a0614a)"></div>
  <div class="photo" role="img" aria-label="Grey slate roof beside brick wall" style="left:35px;top:264px;width:167px;height:115px;background:linear-gradient(180deg,#9b6a52,#8d8f93)"></div>
  <div class="photo" role="img" aria-label="Conical slate turret roof among trees" style="left:211px;top:143px;width:135px;height:236px;background:linear-gradient(180deg,#6d8a4c,#7a7885 55%,#cdbf9a)"></div>
  <div class="photo" role="img" aria-label="House with new slate roof and verandah" style="left:355px;top:143px;width:226px;height:236px;background:linear-gradient(180deg,#b9cbe0,#5d5a60 45%,#4a5c32)"></div>

  <div class="intro">
    <p>At Tallowcrest Slate we specialize in the upkeep, maintenance, repair and replacement of all types of slate roof as well as wood shingles.&nbsp; We can track down the leak that just won't go away or give your house a complete re-roof. We can also provide all your guttering needs.</p>
    <p>Tallowcrest Slate is a small company and as such we do not have the overheads that larger companies do.&nbsp; Quality work and attention to detail are our trademark.</p>
    <p>All photos on this website consist of work which I have personally done.&nbsp; The above photos provide at a quick glance a reasonable cross section of the type of work I do.</p>
    <p>By clicking on the Photo Gallery link you can see other work including some before and after shots.</p>
  </div>

  <aside class="sidebar">
    <h2>Call now and arrange a free quote:</h2>
    <p class="area">We service all inner city suburbs of Sydney roughly covering an area encompassing Gordon to Epping, Mosman to Bondi, Coogee to Kogarah and Kingsgrove to Burwood and Concord</p>
    <div class="contacts">
      <div class="contact-line"><span class="label">Mobile:</span> 0427618392</div>
      <div class="contact-line"><span class="label">Fax:</span> 02 81443071</div>
    </div>
    <p class="reg">Abn 47 309 216 884<br>Lic No. 208734C</p>
  </aside>

  <nav class="nav nav-bottom">
    <a class="active">Home</a><span class="sep"></span><a>Slate Roof Repairs</a><span class="sep"></span><a>Slate Reroofing</a><span class="sep"></span><a>Slate Roof Benefits</a><span class="sep"></span><a>Other Services</a><span class="sep"></span><a>Photo Gallery</a><span class="sep"></span><a>FAQ's</a><span class="sep"></span><a>Free Quote</a><span class="sep"></span><a>Contact Us</a>
  </nav>
</div>

<p class="copyright">© 2009 Tallowcrest Slate. All Rights Reserved.</p>
</body>
</html>
```